Create Lanternfield HR Business Cards.

Create Business Cards for Lanternfield HR. 2 sided and Would like the back to have the logo.

Info for Business Card:
Address: 4827 Millbrook Ave Suite 230 Cleveland, Ohio 44987
Office Number: 216-555-0143
Mobile: 216-555-0192

Website: www.lanternfieldhr.example

Target Market(s)

Small to medium size businesses

Industry/Entity Type

Human Resources

Contact Information for Business Card

Company logo and information

Font styles to use
Serif
Sans Serif

Requirements
Must have
• Info for Business Card: Address: 4827 Millbrook Ave Suite 230 Cleveland, Ohio 44987 Office Number: 216-555-0143 Mobile: 216-555-0192 Website: www.lanternfieldhr.example

```html
<!DOCTYPE html>
<html lang="en">
<head>
<meta charset="utf-8">
<title>Lanternfield HR – Business Cards</title>
<link rel="stylesheet" href="https://fonts.googleapis.com/css2?family=Poppins:wght@500;600&display=swap">
<style>
  :root {
    --navy: #3f3576;
    --navy-deep: #111338;
    --orange: #f08a2c;
    --orange-deep: #e0622a;
    --paper: #f4f4f4;
    --paper-shade: #dcdee2;
    --backdrop: #ece6da;
  }
  * { margin: 0; padding: 0; box-sizing: border-box; }
  html, body { width: 1200px; height: 866px; overflow: hidden; }
  body {
    background: var(--backdrop);
    font-family: "Poppins", sans-serif;
    position: relative;
  }
  .card {
    position: absolute;
    top: 304px;
    width: 400px;
    height: 258px;
    overflow: hidden;
  }
  .card--front { left: 175px; background: linear-gradient(180deg, var(--navy) 40%, var(--navy-deep) 100%); }
  .card--back  { left: 625px; background: linear-gradient(180deg, var(--navy) 50%, var(--navy-deep) 100%); }

  .info-panel {
    position: absolute;
    left: 0; top: 0;
    width: 233px; height: 247px;
    background: linear-gradient(180deg, var(--paper) 30%, var(--paper-shade) 100%);
  }
  .brand {
    position: absolute;
    left: 28px; top: 42px;
    display: flex; align-items: center; gap: 7px;
    font-weight: 600; font-size: 15px; color: var(--navy);
  }
  .brand__dot { width: 11px; height: 11px; border-radius: 50%; background: var(--orange); }

  .contact-list { position: absolute; left: 23px; top: 126px; list-style: none; }
  .contact-list li {
    display: flex; align-items: flex-start; gap: 10px;
    font-weight: 500; font-size: 12px; line-height: 15px;
    color: var(--navy-deep); margin-bottom: 8.5px;
    white-space: nowrap;
  }
  .contact-icon {
    flex: none; width: 16px; height: 16px; border-radius: 50%;
    background: var(--orange-deep);
    display: flex; align-items: center; justify-content: center;
  }
  .contact-icon svg { width: 10px; height: 10px; }

  .front-decor {
    position: absolute;
    left: 294px; top: 0;
    width: 106px; height: 247px;
    background: linear-gradient(180deg, var(--paper) 20%, var(--paper-shade) 100%);
  }
  .front-band {
    position: absolute; left: 0; bottom: 0;
    width: 100%; height: 11px; background: var(--navy-deep);
  }

  .back-decor {
    position: absolute;
    left: 0; top: 0;
    width: 125px; height: 100%;
    background: linear-gradient(180deg, var(--orange) 40%, var(--orange-deep) 100%);
  }
  .back-band {
    position: absolute; left: 0; bottom: 0;
    width: 100%; height: 10px;
    background: linear-gradient(90deg, var(--orange-deep), var(--orange));
  }
  .back-brand {
    position: absolute; right: 22px; bottom: 46px;
    display: flex; align-items: center; gap: 8px;
    font-weight: 600; font-size: 19px; color: #ffffff;
  }
  .back-brand__dot { width: 14px; height: 14px; border-radius: 50%; background: var(--orange); }
</style>
</head>
<body>
  <section class="card card--front" aria-label="Business card front">
    <div class="info-panel">
      <div class="brand"><span class="brand__dot"></span>Lanternfield HR</div>
      <ul class="contact-list">
        <li>
          <span class="contact-icon"><svg viewBox="0 0 24 24"><rect x="7" y="2" width="10" height="20" rx="2" fill="none" stroke="#fff" stroke-width="2.4"/><circle cx="12" cy="18" r="1.3" fill="#fff"/></svg></span>
          216-555-0192
        </li>
        <li>
          <span class="contact-icon"><svg viewBox="0 0 24 24"><path fill="#fff" d="M6.6 10.8a15 15 0 0 0 6.6 6.6l2.2-2.2c.3-.3.7-.4 1-.2 1.1.4 2.3.6 3.6.6.6 0 1 .4 1 1V20c0 .6-.4 1-1 1A17 17 0 0 1 3 4c0-.6.4-1 1-1h3.5c.6 0 1 .4 1 1 0 1.3.2 2.5.6 3.6.1.3 0 .7-.2 1z"/></svg></span>
          216-555-0143
        </li>
        <li>
          <span class="contact-icon"><svg viewBox="0 0 24 24" fill="none" stroke="#fff" stroke-width="2"><circle cx="12" cy="12" r="9"/><ellipse cx="12" cy="12" rx="4" ry="9"/><path d="M3 12h18"/></svg></span>
          www.lanternfieldhr.example
        </li>
        <li>
          <span class="contact-icon"><svg viewBox="0 0 24 24"><path fill="none" stroke="#fff" stroke-width="2.4" d="M12 21s-6-6-6-11a6 6 0 0 1 12 0c0 5-6 11-6 11z"/><circle cx="12" cy="10" r="2" fill="#fff"/></svg></span>
          <span>4827 Millbrook Ave Suite<br>230 Cleveland, Ohio 44987</span>
        </li>
      </ul>
    </div>
    <div class="front-decor" role="img" aria-label="Large brand letter decoration in light grey"></div>
    <div class="front-band"></div>
  </section>

  <section class="card card--back" aria-label="Business card back">
    <div class="back-decor" role="img" aria-label="Large brand letter decoration in orange"></div>
    <div class="back-brand"><span class="back-brand__dot"></span>Lanternfield HR</div>
    <div class="back-band"></div>
  </section>
</body>
</html>
```